Design an Advertisement - Valet Auto Wash Service

I am looking for a simple car wash flyer designed for Instagram and Facebook posts.

Information for the flyer is attached in pdf. I've also attached a simple flyer I made with all the information in the pdf. Use it for content reference.

This design is for a Valet Auto Wash Service.

Attached files:
1. pdf of information
2. sample flyer I designed (use as content reference)
3. hillcrestgo logo. (feel free to include this).

```html
<!DOCTYPE html>
<html lang="en">
<head>
<meta charset="utf-8">
<title>Valet Auto Wash Service</title>
<link href="https://fonts.googleapis.com/css2?family=Montserrat:wght@400;500;700;800&family=Great+Vibes&display=swap" rel="stylesheet">
<style>
  :root {
    --rose: #c8525e;
    --blush: #ebc1c6;
    --teal: #4a7588;
    --white: #ffffff;
  }
  * { box-sizing: border-box; margin: 0; padding: 0; }
  html, body { width: 1200px; height: 1200px; overflow: hidden; }
  body { font-family: "Montserrat", sans-serif; background: var(--rose); }
  .flyer { position: relative; width: 1200px; height: 1200px; background: var(--rose); }
  .frame {
    position: absolute; left: 20px; top: 20px; right: 20px; bottom: 20px;
    border: 4px solid var(--white); border-radius: 12px;
  }
  .headline-main {
    position: absolute; left: 0; width: 830px; top: 80px; text-align: center;
    color: var(--white); font-weight: 800; font-size: 100px; letter-spacing: 1px; line-height: 1;
  }
  .headline-sub {
    position: absolute; left: 53px; top: 198px;
    color: var(--teal); font-weight: 500; font-size: 66px; line-height: 1;
  }
  .brand-mark {
    position: absolute; left: 847px; top: 63px; width: 274px; height: 274px;
    border-radius: 50%; background: var(--teal);
    display: flex; align-items: center; justify-content: center;
  }
  .brand-name { color: var(--white); font-weight: 700; font-size: 34px; }
  .price-table {
    position: absolute; left: 56px; top: 368px; width: 1079px; height: 525px;
    background: var(--blush); border-radius: 10px; overflow: hidden;
    display: grid;
    grid-template-columns: 212px 133px 367px 1fr;
    grid-template-rows: 53px 1fr 1fr 1fr;
    color: var(--teal);
  }
  .cell {
    display: flex; align-items: center; justify-content: center; text-align: center;
    border-right: 2px solid var(--rose); border-bottom: 2px solid var(--rose);
  }
  .cell.last-col { border-right: none; }
  .cell.last-row { border-bottom: none; }
  .head { color: var(--white); font-size: 20px; text-transform: uppercase; }
  .tier, .charge { font-size: 25px; line-height: 1.35; }
  .features { grid-row: 2 / 5; flex-direction: column; gap: 30px; font-size: 21px; border-bottom: none; }
  .notes {
    position: absolute; left: 60px; top: 914px; width: 1010px;
    color: var(--white); font-size: 25px; line-height: 1.36;
  }
  .contact-box {
    position: absolute; left: 147px; top: 1033px; width: 509px; height: 116px;
    background: var(--blush); border-radius: 10px; color: var(--teal);
    display: flex; flex-direction: column; align-items: center; justify-content: center;
    font-size: 32px; line-height: 1.3;
  }
  .tagline {
    position: absolute; left: 772px; top: 1072px; width: 388px; text-align: center;
    color: var(--white); font-family: "Great Vibes", cursive; font-size: 74px; line-height: 1;
  }
</style>
</head>
<body>
<div class="flyer">
  <div class="frame"></div>

  <h1 class="headline-main">VALET</h1>
  <h2 class="headline-sub">AUTO WASH SERVICE</h2>

  <div class="brand-mark"><span class="brand-name">hillcrestgo</span></div>

  <div class="price-table">
    <div class="cell head">Services</div>
    <div class="cell head">Charge</div>
    <div class="cell head">Interior</div>
    <div class="cell head last-col">Exterior</div>

    <div class="cell tier">SEDAN/SMALL</div>
    <div class="cell charge">$60</div>
    <div class="cell features" style="grid-column:3;">
      <span>Interior vacuum (carpet &amp; seats)</span>
      <span>Floor mats light clean</span>
      <span>Interior panels basic clean</span>
      <span>Window and wind shield clean</span>
    </div>
    <div class="cell features last-col" style="grid-column:4;">
      <span>Exterior wash</span>
      <span>Exterior towel dry</span>
      <span>Tire wash and shine</span>
    </div>

    <div class="cell tier" style="grid-column:1;grid-row:3;">MIDSIZE SUV</div>
    <div class="cell charge" style="grid-column:2;grid-row:3;">$70</div>

    <div class="cell tier last-row" style="grid-column:1;grid-row:4;">FULL<br>SUV/TRUCK</div>
    <div class="cell charge last-row" style="grid-column:2;grid-row:4;">$80</div>
  </div>

  <div class="notes">
    <p>*All categories are valet serviced - i.e. clients car will be picked up, detailed, and delivered to the client.</p>
    <p>*All appointments should be made at least 24hrs before pick-up.</p>
  </div>

  <div class="contact-box">
    <span>Mira - 3065550147</span>
    <span>hillcrestgo@example.com</span>
  </div>

  <p class="tagline">Time to Shine</p>
</div>
</body>
</html>
```